Computer Company needs a Business card design

We need a business card design for our business. We assist people to transition to the QLX (Quorra Linkwave Exchange). The Australian Government-owned qlx™ network is a brand new telecommunications network currently being rolled out across Australia, giving access to a reliable broadband connection. Our niche market will predominantly be domestic customers in the 50+ age bracket. The assistance that we provide is everything from arranging the equipment, arranging the plan and contract term, appointment times, final testing of the network and any tweaks that need to be made. We basically PM the transition from start to finish. The business card design should be minimalist, should communicate loyalty and stability, should be easy to read and clearly explain what we do. We have asked for front and back. However, the back of the card does not have to include much information at all. It could be just a small design, or a repeat of our phone number. Up to you. The attached file only says what is required on the card. It does not specify where to arrange the text, what fonts to use, etc etc. As much as we would like to give you more info, due to our very limited design ability, we are not really able to send you any rough, or otherwise, designs of what we are after. Hopefully the above description is enough for you.

```html
<!DOCTYPE html>
<html lang="en">
<head>
<meta charset="utf-8">
<title>QLX Assist – Business Card</title>
<link rel="stylesheet" href="https://fonts.googleapis.com/css2?family=Montserrat:wght@400;500;600;700&display=swap">
<style>
  :root{
    --stage:#e9eaec;
    --card-white:#ffffff;
    --charcoal:#414143;
    --brand-blue:#1f74bd;
    --navy:#104a76;
    --deep-navy:#0d3f66;
    --tab-top:#3a8fc8;
    --tab-bottom:#4058a8;
    --teal:#28a6c8;
    --ink-light:#ffffff;
    --ink-dark:#3a3a3c;
  }
  html,body{margin:0;padding:0;width:1200px;height:966px;overflow:hidden;background:var(--stage);}
  .stage{position:relative;width:1200px;height:966px;}
  .card{position:absolute;width:694px;height:370px;display:block;}
  .card--front{left:136px;top:101px;}
  .card--back{left:368px;top:510px;}
  .card text{font-family:'Montserrat',sans-serif;}
  .front-name{font-weight:500;font-size:35px;fill:var(--ink-light);}
  .front-detail{font-weight:500;font-size:18px;fill:var(--ink-light);}
  .brand-name{font-weight:700;font-size:42px;fill:var(--brand-blue);}
  .brand-tag{font-weight:500;font-size:16px;fill:var(--ink-dark);letter-spacing:.5px;}
  .back-brand{font-weight:700;font-size:54px;fill:var(--brand-blue);}
  .back-phone{font-weight:500;font-size:38px;fill:var(--ink-light);letter-spacing:1px;}
</style>
</head>
<body>
<main class="stage">

  <!-- Front of card -->
  <svg class="card card--front" viewBox="0 0 862 460" role="group" aria-label="Business card front">
    <defs>
      <linearGradient id="tabGradient" x1="0" y1="0" x2="0" y2="1">
        <stop offset="0" stop-color="var(--tab-top)"/>
        <stop offset="1" stop-color="var(--tab-bottom)"/>
      </linearGradient>
      <linearGradient id="arcGradient" x1="0" y1="0" x2="0" y2="1">
        <stop offset="0" stop-color="var(--teal)"/>
        <stop offset="1" stop-color="var(--tab-bottom)"/>
      </linearGradient>
    </defs>
    <rect class="card-base" width="862" height="460" fill="var(--card-white)"/>
    <path class="dark-panel" d="M0 0 H270 C360 60 400 170 440 270 C480 360 500 410 537 460 H0 Z" fill="var(--charcoal)"/>
    <path class="edge-band" d="M835 245 C850 290 862 310 862 320 V460 H842 C852 380 850 300 835 245 Z" fill="var(--charcoal)"/>
    <path class="edge-arc" d="M788 128 C830 200 835 300 826 360 C818 410 800 440 772 460 H842 C850 400 855 300 830 230 C815 185 800 150 788 128 Z" fill="url(#arcGradient)"/>

    <path class="name-tab" d="M0 0 H44 V193 A22 22 0 0 1 22 215 A22 22 0 0 1 0 193 Z" fill="url(#tabGradient)"/>
    <g class="icon-person" fill="var(--ink-light)">
      <circle cx="22" cy="185" r="5"/>
      <path d="M12 201 C12 193 16 191 22 191 C28 191 32 193 32 201 Z"/>
    </g>

    <text class="front-name" x="70" y="174">Dale Morrow</text>

    <circle class="icon-disc" cx="66" cy="268" r="15" fill="url(#tabGradient)"/>
    <g class="icon-phone" fill="var(--ink-light)">
      <path d="M58 264 C58 260 74 260 74 264 L74 266 L70 266 L70 264 L62 264 L62 266 L58 266 Z"/>
      <rect x="61" y="267" width="10" height="7" rx="1"/>
    </g>
    <text class="front-detail" x="103" y="275">0491578203</text>

    <circle class="icon-disc" cx="66" cy="315" r="15" fill="url(#tabGradient)"/>
    <g class="icon-globe" fill="none" stroke="var(--ink-light)" stroke-width="1.3">
      <circle cx="66" cy="315" r="7"/>
      <ellipse cx="66" cy="315" rx="3" ry="7"/>
      <line x1="59" y1="315" x2="73" y2="315"/>
    </g>
    <text class="front-detail" x="99" y="321">www.qlxassist.com.au</text>

    <g class="brand-lockup">
      <text class="brand-name" x="480" y="212">QLX ASSIST</text>
      <circle cx="762" cy="197" r="18" fill="var(--brand-blue)"/>
      <text class="brand-tag" x="482" y="244">HOME CONNECTION HELP</text>
    </g>
  </svg>

  <!-- Back of card -->
  <svg class="card card--back" viewBox="0 0 862 460" role="group" aria-label="Business card back">
    <rect class="card-base" width="862" height="460" fill="var(--card-white)"/>
    <path class="left-band" d="M0 0 H40 C20 70 14 150 20 230 L0 190 Z" fill="var(--deep-navy)"/>
    <path class="left-arc" d="M40 0 H142 C70 70 42 170 48 250 C54 310 70 360 95 397 C60 350 30 290 20 230 C14 150 20 70 40 0 Z" fill="var(--brand-blue)"/>
    <path class="right-panel" d="M675 0 H862 V460 H415 C500 380 540 280 580 180 C620 80 640 40 675 0 Z" fill="var(--navy)"/>

    <g class="brand-lockup">
      <text class="back-brand" x="112" y="230">QLX ASSIST</text>
      <circle cx="455" cy="212" r="22" fill="var(--brand-blue)"/>
    </g>

    <g class="icon-phone-square">
      <rect x="545" y="365" width="32" height="32" rx="5" fill="var(--ink-light)"/>
      <path d="M553 372 L558 371 L561 378 L558 380 C560 385 563 388 568 390 L570 387 L577 390 L576 395 C566 395 553 384 553 372 Z" fill="var(--navy)"/>
    </g>
    <text class="back-phone" x="588" y="396">0491578203</text>
  </svg>

</main>
</body>
</html>
```